Luxury Toilet Rental Business. Wavelet Hire.

Wavelet Hire (the logo is in the uploaded files)
We RENT and SELL Luxury Trailer toilets.
- Show location, number, pricing, pictures.
- We have two stall trailers for rent AND 3 stall trailers
- We sell them too
- We want our phone number shown
- We are a local company
- Slogan: Elevate your event with Wavelet Hire. The Luxurious Loo
- We want a pricing portion
- We want the sizes shown
- We want the different rates/ prices shown
- We do 1 day rentals
- We do 1 week rentals
- We want the service area. We serve Los Angeles County, Orange County, Riverside County, San Bernardino County, and Palm Desert.
- Our location is in Santa Ana California

Target Market(s)

Event planners, wedding planners, venue planners, concerts, events, gatherings.

Industry/Entity Type

Luxury Toilet Rentals

Number of Pages Required

1 page

Font styles to use
Serif
Sans Serif

Colors
EE7325
F08F49
F5BC92
FAE3D3
FDF4ED

Requirements
Must have
• Location, pricing, pictures, available areas. Our slogan.
Nice to have
• I like the idea of having tabs that show price, a tab that shows our contact information, pictures, event ideas, and where we service (the areas we'll go to)

```html
<!DOCTYPE html>
<html lang="en">
<head>
<meta charset="utf-8">
<title>Wavelet Hire – Luxury Trailer Toilets</title>
<link rel="stylesheet" href="https://fonts.googleapis.com/css2?family=Montserrat:wght@200;300;400;600;700&family=Oswald:wght@400&display=swap">
<style>
:root{
  --board:#eb6a24;
  --orange:#ee7325;
  --slate:#58585a;
  --slate-deep:#4f4f52;
  --card-head:#d9d9d9;
  --white:#ffffff;
  --ink:#3a3a3c;
  --rule:#c9c9c9;
}
*{margin:0;padding:0;box-sizing:border-box}
html,body{width:1200px;height:849px;overflow:hidden;background:var(--board);font-family:"Montserrat",sans-serif}
.canvas{position:relative;width:1200px;height:849px}
.abs{position:absolute}

/* home page */
.home{left:73px;top:22px;width:527px;height:805px;background:var(--white);overflow:hidden}
.header-brand{left:0;top:0;width:263px;height:47px;background:var(--white)}
.brand{left:36px;top:14px;display:flex;align-items:center;gap:6px;color:var(--orange);font-weight:700;font-size:14px;letter-spacing:.5px}
.brand-square{width:11px;height:11px;background:var(--orange)}
.header-nav{left:263px;top:0;width:264px;height:47px;background:var(--slate)}
.menu{left:168px;top:13px;display:flex;align-items:center;gap:8px;color:var(--white);font-family:"Oswald",sans-serif;font-size:14px}
.hero-copy{left:0;top:47px;width:263px;height:288px;background:var(--slate)}
.hero-title{left:34px;top:42px;color:var(--white);font-weight:200;font-size:24px;line-height:24px}
.hero-sub{left:34px;top:127px;color:var(--white);font-weight:300;font-size:12.5px;line-height:16px}
.body-s{color:var(--white);font-weight:300;font-size:7px;line-height:9.3px}
.hero-body{left:34px;top:166px;width:175px}
.btn{border:1.5px solid var(--orange);border-radius:12px;color:var(--white);font-weight:400;display:flex;align-items:center;justify-content:center}
.hero-btn{left:34px;top:247px;width:83px;height:19px;font-size:7.5px}
.hero-media{left:263px;top:47px;width:264px;height:288px;background:linear-gradient(160deg,#3d3a48,#4a3f58 50%,#3a3840)}
.watch{left:0;width:264px;top:165px;text-align:center;color:var(--white);font-weight:300;font-size:8px}
.stats{left:0;top:335px;width:527px;height:161px;background:linear-gradient(120deg,#5e5e61,#707073 55%,#666669)}
.stat{top:42px;width:110px;text-align:center;color:var(--white)}
.stat-label{font-weight:600;font-size:8.5px;line-height:9px;margin-top:3px}
.stat-num{font-weight:200;font-size:27px;line-height:30px}
.feature-photo{left:0;top:496px;width:262px;height:289px;background:linear-gradient(180deg,#8a8b8e,#6d6e72 45%,#8f9093)}
.feature-copy{left:262px;top:496px;width:265px;height:289px;background:var(--slate)}
.feature-title{left:29px;top:94px;color:var(--white);font-weight:300;font-size:16px;line-height:20px}
.feature-body{left:28px;top:138px;width:215px;color:var(--white);font-weight:300;font-size:9.3px;line-height:11.5px}
.feature-btn{left:28px;top:210px;width:83px;height:19px;font-size:8px}

/* detail page */
.detail{left:636px;top:27px;width:432px;height:800px;background:var(--white);overflow:hidden}
.section-head{left:0;width:432px;text-align:center;color:var(--ink)}
.section-head .rule{width:50px;height:1px;background:var(--ink);margin:0 auto 5px}
.section-head h2{font-weight:300;font-size:16px;line-height:18px}
.section-head p{font-weight:300;font-size:5.5px;margin-top:2px}
.thumb{height:78px;width:138px}
.about-copy{left:0;top:248px;width:218px;height:236px;background:var(--slate)}
.about-title{left:24px;top:68px;color:var(--white);font-weight:300;font-size:12.5px;line-height:16px}
.about-body{left:23px;top:111px;width:175px}
.about-btn{left:23px;top:171px;width:68px;height:15px;font-size:6.5px}
.about-photo{left:218px;top:248px;width:214px;height:236px;background:linear-gradient(170deg,#b9b7ae,#8d8e90 45%,#a9aaab)}
.card{top:571px;width:122px;height:157px;background:var(--slate)}
.card-head{height:40px;background:var(--card-head);display:flex;align-items:center;justify-content:center;color:var(--ink);font-weight:600;font-size:16px}
.card ul{list-style:none;margin:25px 0 0 22px;width:66px}
.card li{position:relative;color:var(--white);font-weight:300;font-size:7.5px;line-height:9px;padding:3px 0 2px 9px;border-bottom:1px solid var(--rule)}
.card li:first-child{border-bottom:none}
.card li::before{content:"";position:absolute;left:-1px;top:6px;width:3.5px;height:3.5px;background:var(--orange)}
</style>
</head>
<body>
<div class="canvas">

  <section class="abs home">
    <div class="abs header-brand">
      <div class="abs brand"><span class="brand-square"></span>Wavelet Hire</div>
    </div>
    <div class="abs header-nav">
      <div class="abs menu">MENU
        <svg width="22" height="18" viewBox="0 0 22 18"><rect y="0" width="22" height="2.4" fill="#fff"/><rect y="5.2" width="22" height="2.4" fill="#fff"/><rect y="10.4" width="22" height="2.4" fill="#fff"/><rect y="15.6" width="22" height="2.4" fill="#fff"/></svg>
      </div>
    </div>

    <div class="abs hero-copy">
      <h1 class="abs hero-title">We RENT and<br>SELL Luxury<br>Trailer toilets.</h1>
      <p class="abs hero-sub">Elevate your event with<br>The Luxurious Loo</p>
      <p class="abs body-s hero-body">We lease, rent and sell one of its own kind luxury toilets and modile loos. We are proud to have the highest standrds of excellence and luxurious facilities in the market and operate with excellence.</p>
      <a class="abs btn hero-btn">Learn More....</a>
    </div>
    <div class="abs hero-media" role="img" aria-label="Dimly lit interior of a luxury trailer restroom with sinks and dispensers">
      <svg class="abs" style="left:108px;top:108px" width="50" height="50" viewBox="0 0 50 50">
        <circle cx="25" cy="25" r="24" fill="#6a6470" opacity=".8"/>
        <circle cx="25" cy="25" r="20" fill="var(--orange)"/>
        <path d="M20 15 L34 25 L20 35 Z" fill="#fff"/>
      </svg>
      <p class="abs watch">Watch Our Video</p>
    </div>

    <div class="abs stats" role="img" aria-label="Faded photo of a restroom interior behind company figures">
      <div class="abs stat" style="left:53px">
        <svg width="22" height="24" viewBox="0 0 22 24"><path d="M2 11h4v12H2z M8 11 L12 2 c2 0 3 1 3 3 l-1 5 h6 c1 0 2 1 1.6 2.4 L19 21 c-.4 1.3-1.4 2-2.6 2H8z" fill="var(--orange)"/></svg>
        <div class="stat-label">Customers<br>Serviced</div>
        <div class="stat-num">567</div>
      </div>
      <div class="abs stat" style="left:168px">
        <svg width="20" height="24" viewBox="0 0 20 24"><rect x="2" y="3" width="16" height="21" fill="none" stroke="var(--orange)" stroke-width="2"/><rect x="6" y="0" width="8" height="4" fill="var(--orange)"/><g fill="var(--orange)"><rect x="5" y="7" width="2.5" height="2.5"/><rect x="9" y="7" width="2.5" height="2.5"/><rect x="13" y="7" width="2.5" height="2.5"/><rect x="5" y="12" width="2.5" height="2.5"/><rect x="9" y="12" width="2.5" height="2.5"/><rect x="13" y="12" width="2.5" height="2.5"/><rect x="8" y="18" width="4" height="6"/></g></svg>
        <div class="stat-label">Serviced<br>Locations</div>
        <div class="stat-num">04</div>
      </div>
      <div class="abs stat" style="left:279px;top:40px">
        <svg width="26" height="20" viewBox="0 0 26 20"><g fill="none" stroke="var(--orange)" stroke-width="2.6" stroke-linecap="round"><path d="M2 7 Q13 -2 24 7"/><path d="M6 11 Q13 5 20 11"/></g><circle cx="13" cy="16" r="2.6" fill="var(--orange)"/></svg>
        <div class="stat-label">Owned<br>Toilets</div>
        <div class="stat-num">82</div>
      </div>
      <div class="abs stat" style="left:381px">
        <svg width="20" height="24" viewBox="0 0 20 24"><path d="M2 2h16v10c0 6-4 9-8 11-4-2-8-5-8-11z" fill="var(--orange)"/><path d="M10 5v15c-3-1.5-5-4-5-8V5z" fill="#6b6b6e"/></svg>
        <div class="stat-label">Sales<br>Performed</div>
        <div class="stat-num">1643</div>
      </div>
    </div>

    <div class="abs feature-photo" role="img" aria-label="Grey three-stall toilet trailer with blue steps parked outside a warehouse"></div>
    <div class="abs feature-copy">
      <h2 class="abs feature-title">Elevate your event with<br>The Luxurious Loo</h2>
      <p class="abs feature-body">We lease, rent and sell one of its own kind luxury toilets and modile loos. We are proud to have the highest standrds of excellence and luxurious facilities in the market and operate with excellence.</p>
      <a class="abs btn feature-btn">Learn More....</a>
    </div>
  </section>

  <section class="abs detail">
    <header class="abs section-head" style="top:13px">
      <div class="rule"></div>
      <h2>Our Luxury Toilet Gallery</h2>
      <p>Take alook at our range of luxury toilets and hihg end loos</p>
    </header>
    <div class="abs thumb" style="left:0;top:57px;background:linear-gradient(150deg,#e8e8e6,#bdbcb8)" role="img" aria-label="Trailer restroom vanity with white basin"></div>
    <div class="abs thumb" style="left:145px;top:57px;background:linear-gradient(150deg,#ededeb,#c3c1bc)" role="img" aria-label="Restroom sink and cabinet inside trailer"></div>
    <div class="abs thumb" style="left:293px;top:57px;background:linear-gradient(180deg,#b6b5ad,#8c8c8c 55%,#9d9d9d)" role="img" aria-label="Toilet trailer parked in a factory yard"></div>
    <div class="abs thumb" style="left:0;top:146px;background:linear-gradient(180deg,#b3b2ac,#8a8a8b 55%,#9a9a9a)" role="img" aria-label="Two-stall toilet trailer with steps, side view"></div>
    <div class="abs thumb" style="left:145px;top:146px;background:linear-gradient(150deg,#e9e9e9,#bfc4c7)" role="img" aria-label="Compact trailer restroom with toilet and sink"></div>
    <div class="abs thumb" style="left:293px;top:146px;background:linear-gradient(150deg,#ececec,#c8c7c2)" role="img" aria-label="White toilet stall with mirror and cabinet"></div>

    <div class="abs about-copy">
      <h2 class="abs about-title">Elevate your event with<br>The Luxurious Loo</h2>
      <p class="abs body-s about-body">We lease, rent and sell one of its own kind luxury toilets and modile loos. We are proud to have the highest standrds of excellence and luxurious facilities in the market and operate with excellence.</p>
      <a class="abs btn about-btn">Learn More....</a>
    </div>
    <div class="abs about-photo" role="img" aria-label="Two-stall grey toilet trailer with fold-down steps"></div>

    <header class="abs section-head" style="top:524px">
      <div class="rule"></div>
      <h2>Our Pricing</h2>
      <p>How much can you get one of these with us?</p>
    </header>
    <div class="abs card" style="left:25px">
      <div class="card-head">$5999.00</div>
      <ul><li>5 Days</li><li>Double Toilet</li><li>Full Service</li><li>Attendant</li></ul>
    </div>
    <div class="abs card" style="left:157px">
      <div class="card-head">$7999.00</div>
      <ul><li>5 Days</li><li>Double Toilet</li><li>Full Service</li><li>Attendant</li></ul>
    </div>
    <div class="abs card" style="left:288px">
      <div class="card-head">$2999.00</div>
      <ul><li>5 Days</li><li>Double Toilet</li><li>Full Service</li><li>Attendant</li></ul>
    </div>

    <header class="abs section-head" style="top:760px;left:-4px">
      <div class="rule"></div>
      <h2>The places we serve</h2>
      <p>Where do we operate business?</p>
    </header>
  </section>

</div>
</body>
</html>
```